Brambleway Business Card

I have a business that is called "Brambleway Electrical Goods LTD" My company deals with top of the range laptops and mobile phones that are exclusive. I need a business card that will be eye catching but not over complicated.

Target Market(s)

Adults aged 19 to 50
Upper middle class

Industry/Entity Type

Business

Requirements
Must have
• Company name/logo (file attached)
• It must have my contact information which is:

• Name: Dale Margrove

• Position: Managing Director 

• Business Address: 7 Haddon Row, London, W4 9QZ

• Contact Number: 02085519304
• Mobile: 07815206473
• Email: info@brambleway-goods.co.uk
Nice to have
• Simple and stylish
• Eye catching

```html
<!DOCTYPE html>
<html lang="en">
<head>
<meta charset="utf-8">
<title>Brambleway Electrical Goods – Business Card</title>
<link rel="stylesheet" href="https://fonts.googleapis.com/css2?family=Mulish:wght@300;400;700;800&display=swap">
<style>
  :root {
    --card-bg: #165a76;
    --card-bg-deep: #114f69;
    --frame: #ffffff;
    --text: #ffffff;
    --brand: #52e2ee;
    --disc-light: #1f6d8a;
    --disc-dark: #155670;
  }
  html, body {
    margin: 0;
    padding: 0;
    width: 1200px;
    height: 686px;
    overflow: hidden;
    background: var(--card-bg);
  }
  .card {
    position: relative;
    width: 1200px;
    height: 686px;
    overflow: hidden;
    background: linear-gradient(160deg, var(--card-bg) 0%, var(--card-bg-deep) 100%);
    font-family: "Mulish", "Century Gothic", sans-serif;
    color: var(--text);
  }
  .card__disc {
    position: absolute;
    left: 0;
    top: 0;
    width: 480px;
    height: 380px;
  }
  .card__frame {
    position: absolute;
    left: 23px;
    top: 23px;
    width: 1148px;
    height: 634px;
    border: 3px solid var(--frame);
  }
  .card__text {
    position: absolute;
    margin: 0;
    line-height: 1;
    white-space: nowrap;
  }
  .brand-name {
    right: 60px;
    top: 104px;
    font-size: 98px;
    font-weight: 300;
    letter-spacing: 1px;
    color: var(--brand);
  }
  .brand-tagline {
    right: 66px;
    top: 258px;
    font-size: 60px;
    font-weight: 700;
  }
  .brand-address {
    right: 70px;
    top: 337px;
    font-size: 28px;
    font-weight: 400;
  }
  .person-name {
    left: 64px;
    top: 400px;
    font-size: 58px;
    font-weight: 700;
  }
  .person-role {
    left: 268px;
    top: 478px;
    font-size: 27px;
    font-weight: 700;
  }
  .contact-email {
    left: 63px;
    top: 613px;
    font-size: 32px;
    font-weight: 400;
  }
  .contact-list {
    position: absolute;
    left: 643px;
    top: 548px;
    margin: 0;
    display: grid;
    grid-template-columns: auto auto;
    column-gap: 14px;
    row-gap: 14px;
    font-size: 42px;
    line-height: 1;
  }
  .contact-list dt { font-weight: 800; margin: 0; }
  .contact-list dd { font-weight: 400; margin: 0; }
</style>
</head>
<body>
  <div class="card">
    <svg class="card__disc" viewBox="0 0 480 380" role="img" aria-label="Decorative circle with a faint circuit-like texture">
      <defs>
        <radialGradient id="discFill" cx="40%" cy="35%" r="70%">
          <stop offset="0%" stop-color="#1d6784"/>
          <stop offset="100%" stop-color="#175b75"/>
        </radialGradient>
        <filter id="discShadow" x="-20%" y="-20%" width="140%" height="140%">
          <feDropShadow dx="8" dy="10" stdDeviation="10" flood-color="#0a3446" flood-opacity="0.6"/>
        </filter>
      </defs>
      <circle cx="234" cy="126" r="211" fill="url(#discFill)" filter="url(#discShadow)"/>
    </svg>

    <div class="card__frame"></div>

    <p class="card__text brand-name">BRAMBLEWAY</p>
    <p class="card__text brand-tagline">Electrical Goods</p>
    <p class="card__text brand-address">7 Haddon Row, London W4 9QZ</p>

    <p class="card__text person-name">Dale Margrove</p>
    <p class="card__text person-role">Managing Director</p>

    <p class="card__text contact-email">info@brambleway-goods.co.uk</p>

    <dl class="contact-list">
      <dt>Phone:</dt><dd>&nbsp;0 208 551 9304</dd>
      <dt>Mobile:</dt><dd>0 781 520 6473</dd>
    </dl>
  </div>
</body>
</html>
```